Waterproofing Construction company needs letterhead

I need a letterhead design for a commercial waterproofing construction company. We would like to see designs that are contemporary, clean, sleek and use our logo. Our current design is dated. I would also like a cover page (see example) that goes with our letterhead. I would like for the footer to have our address, website, and phone number

Target Market(s)

Customers, potential customers.

Font styles to use
Sans Serif

Requirements
Must have
• logo, website, address, phone numbers, only our colors, tahoma font
• PMS: 295C PMS: 2995C
• CMYK: 100/84/36/39 CMYK: 80/12/1/0
• RGB: 16/44/82 RGB: 0/167/224
• HEX#: #102C52 HEX#: #00A7E0
• Black & White: 100% Black & White: 32%
• Gray Scale: 90% Gray Scale: 32%
Nice to have
• Our "icon" logo attached would be nice somewhere on the page.

```html
<!DOCTYPE html>
<html lang="en">
<head>
<meta charset="utf-8">
<title>Northvale Letterhead</title>
<link href="https://fonts.googleapis.com/css2?family=Lato:wght@400;700;900&family=Yellowtail&display=swap" rel="stylesheet">
<style>
  :root {
    --navy: #102C52;
    --sky: #00A7E0;
    --ink: #4a4a4a;
    --ink-dark: #222222;
    --paper: #ffffff;
    --rule: #9a9a9a;
  }
  * { margin: 0; padding: 0; box-sizing: border-box; }
  html, body { width: 998px; height: 1200px; overflow: hidden; background: var(--paper); }
  .letterhead {
    position: relative;
    width: 998px;
    height: 1200px;
    background: linear-gradient(170deg, #ffffff 40%, #f3f3f3 100%);
    font-family: "Lato", sans-serif;
    color: var(--ink);
  }
  .brand { position: absolute; left: 84px; top: 34px; }
  .brand-name {
    font-weight: 900;
    font-size: 58px;
    line-height: 1;
    color: var(--navy);
    letter-spacing: -1px;
  }
  .brand-tagline {
    margin-top: 10px;
    font-size: 14px;
    color: var(--navy);
    letter-spacing: 0.2px;
  }
  .contact {
    position: absolute;
    left: 771px;
    top: 30px;
    height: 97px;
    padding-left: 17px;
    border-left: 1px solid var(--rule);
    font-size: 12.5px;
    line-height: 1.3;
    color: var(--ink-dark);
  }
  .contact-address { margin-bottom: 8px; }
  .contact-row { display: flex; align-items: center; gap: 6px; height: 21px; }
  .contact-row svg { width: 12px; height: 12px; fill: var(--sky); flex: none; }
  .letter { position: absolute; left: 84px; top: 310px; width: 830px; }
  .salutation { font-weight: 700; font-size: 18.5px; color: var(--navy); margin-bottom: 22px; }
  .letter p {
    font-size: 18px;
    line-height: 27px;
    margin-bottom: 20px;
    text-align: justify;
  }
  .closing { margin-top: 20px; font-size: 21px; color: var(--ink-dark); }
  .signature {
    font-family: "Yellowtail", cursive;
    font-size: 40px;
    color: var(--sky);
    margin-top: 4px;
  }
  .footer { position: absolute; left: 0; bottom: 0; width: 998px; height: 40px; }
  .footer svg { position: absolute; inset: 0; }
  .regions {
    position: absolute;
    left: 669px;
    top: 11px;
    font-size: 13.5px;
    color: #ffffff;
    white-space: nowrap;
  }
  .regions span { margin: 0 5px; }
</style>
</head>
<body>
<main class="letterhead">
  <header>
    <div class="brand">
      <div class="brand-name">Northvale</div>
      <div class="brand-tagline">WATERPROOFING · RESTORATION</div>
    </div>
    <address class="contact" style="font-style:normal">
      <div class="contact-address">PO Box 418<br>Cary Ridge, NC 27019</div>
      <div class="contact-row">
        <svg viewBox="0 0 24 24"><path d="M6.6 10.8a15.1 15.1 0 0 0 6.6 6.6l2.2-2.2a1 1 0 0 1 1-.25 11.4 11.4 0 0 0 3.6.57 1 1 0 0 1 1 1V20a1 1 0 0 1-1 1A17 17 0 0 1 3 4a1 1 0 0 1 1-1h3.5a1 1 0 0 1 1 1c0 1.25.2 2.45.57 3.57a1 1 0 0 1-.25 1z"/></svg>
        (800) 555-0142
      </div>
      <div class="contact-row">
        <svg viewBox="0 0 24 24"><path d="M7 1h10a2 2 0 0 1 2 2v18a2 2 0 0 1-2 2H7a2 2 0 0 1-2-2V3a2 2 0 0 1 2-2zm0 3v14h10V4zm5 15.5a1.2 1.2 0 1 0 0 2.4 1.2 1.2 0 0 0 0-2.4z"/></svg>
        (919) 555-0178
      </div>
      <div class="contact-row">
        <svg viewBox="0 0 24 24"><path d="M12 2a10 10 0 1 0 0 20 10 10 0 0 0 0-20zm6.9 6h-2.9a15.6 15.6 0 0 0-1.4-3.6A8 8 0 0 1 18.9 8zM12 4a14 14 0 0 1 1.9 4h-3.8A14 14 0 0 1 12 4zM4.3 14a8 8 0 0 1 0-4h3.4a16.5 16.5 0 0 0 0 4zm.8 2h2.9a15.6 15.6 0 0 0 1.4 3.6A8 8 0 0 1 5.1 16zM8 8H5.1a8 8 0 0 1 4.3-3.6A15.6 15.6 0 0 0 8 8zm4 12a14 14 0 0 1-1.9-4h3.8A14 14 0 0 1 12 20zm2.3-6H9.7a14.7 14.7 0 0 1 0-4h4.6a14.7 14.7 0 0 1 0 4zm.3 5.6a15.6 15.6 0 0 0 1.4-3.6h2.9a8 8 0 0 1-4.3 3.6zm1.7-5.6a16.5 16.5 0 0 0 0-4h3.4a8 8 0 0 1 0 4z"/></svg>
        www.northvalewp.com
      </div>
    </address>
  </header>

  <section class="letter">
    <div class="salutation">Dear Mr. Lorem,</div>
    <p>Lorem ipsum dolor sit amet, consectetuer adipiscing elit, sed diam nonummy nibh euismod tincidunt ut laoreet dolore magna aliquam erat volutpat. Ut wisi enim ad minim veniam, quis nostrud exerci tation ullamcorper suscipit lobortis nisl ut aliquip ex ea commodo consequat. Duis autem vel eum iriure dolor in hendiusto odio dignissim qui blandit praesent luptatum zzril delenit augue duis dolore te feugait nulla facilisi.</p>
    <p>Lorem ipsum dolor sit amet, consectetuer adipiscing elit, sed diam nonummy nibh euismod tincidunt ut laoreet dolore magna aliquam erat volutpat. Ut wisi enim ad minim veniam, quis nostrud exerci tation ullamcorper suscipit lobortis nisl ut aliquip ex ea commodo consequat. Duis autem vel eum iriure dolor in hendiusto odio dignissim qui blandit praesent luptatum zzril delenit augue duis dolore te feugait nulla facilisi.</p>
    <p>Lorem ipsum dolor sit amet, consectetuer adipiscing elit, sed diam nonummy nibh euismod tincidunt ut laoreet dolore magna aliquam erat volutpat. Ut wisi enim ad minim veniam, quis nostrud exerci tation ullamcorper suscipit lobortis nisl ut aliquip ex ea commodo consequat. Duis autem vel eum iriure dolor in hendiusto odio dignissim qui blandit praesent luptatum zzril delenit augue duis dolore te feugait nulla facilisi.</p>
    <div class="closing">Sincerely Your,</div>
    <div class="signature">Your Name</div>
  </section>

  <footer class="footer">
    <svg width="998" height="40" viewBox="0 0 998 40">
      <polygon points="0,16 612,16 590,38 0,38" fill="var(--navy)"/>
      <polygon points="647,0 998,0 998,40 608,40" fill="var(--sky)"/>
    </svg>
    <div class="regions">North Carolina<span>|</span>South Carolina<span>|</span>Virginia</div>
  </footer>
</main>
</body>
</html>
```